A5 2 sided flyer to promote pharmacy services

We need a leaflet design which promotes our pharmacy and its services. We are a modern, chic hip, funky new pharmacy, and our leaflet should reflect this.
We are looking for an exciting design fun design with limited pictures of people on it.
It needs to be 2 sided, the first side to include name, address, telephone number, twitter and facebook handle, opening hours. I want to highlight our main service with is prescription collection, I like the idea of having a cartoon type image: cartoon 1- ordering prescription, cartoon 2- dispensing medication, cartoon 3- patient collecting prescritpion.
I also need to highlight our services which include
medicine use review
pharmacy first*
Morning after pill*
emergency supply service*
seasonal flu vaccinations*
on the other side i need a consent form for ETP nomination to include full name, address, date of birth, NHS number, signature and current date
this shoudl be on the top half of the leaftet.
On the bottom half or bottom quarter, I need writing:
Thornfield Pharmacy proudly uses a robotic dispensing system.

The Pharmacy directors have invested in this technology to enhance the service that we provide our customers.

Medication is dispensed from a high speed robotic arm within the unit which not only improves efficiency but also importantly maximises patient safety.

The robot in action can be witnessed through a viewing window positioned outside the shop window - it is truly remarkable to see. Please feel free to visit and view. Our staff will be only too happy to introduce you to our new addition and explain how the system works.

Target Market(s)

NHS patients ranging from 16 years to 80 years +

Industry/Entity Type

Pharmacy

Font styles to use
Serif

Requirements
Must have
• Name of pharmacy
• Address of pharmacy: Ashcombe Larkfield Centre, Kestrel Row, Ashcombe, Nottingham, NG4 2TW
• Telephone number:0115 9630587
• Opening times: Mon - Sat 7.30am - 10pm, sunday 8am - 9pm
• Services we offer: Prescription collection service
• minor ailments scheme
• emergency hormonal contraception
• Expert health advice
• Medicines disposal
• Prescription delivery service
• Our twitter handle: ourthornfield
• facebook page: ourthornfieldpharmacy
Nice to have
• colourful, upbeat vibe to the leaflet whilst including all the relevant information.
Should not have
• big pictures of people

```html
<!DOCTYPE html>
<html lang="en">
<head>
<meta charset="utf-8">
<title>Thornfield Pharmacy – Services Flyer</title>
<link rel="stylesheet" href="https://fonts.googleapis.com/css2?family=Alegreya:wght@600;700&family=Alegreya+Sans:ital,wght@1,300;1,400&display=swap">
<style>
  :root {
    --ocean: #0c93cf;
    --aqua: #14edfd;
    --sky: #4abffd;
    --paper: #ffffff;
    --frame: #1b4f8a;
    --heading-cyan: #2ee6ff;
    --item-cyan: #3fdcf5;
    --navy: #15305f;
    --brand: #2d2f8e;
    --brand-dot: #dfe4f7;
  }
  * { margin: 0; padding: 0; box-sizing: border-box; }
  html, body { width: 847px; height: 1200px; overflow: hidden; background: var(--paper); }
  .flyer {
    position: relative;
    width: 847px;
    height: 1200px;
    background: var(--paper);
    overflow: hidden;
  }
  .waves { position: absolute; inset: 0; }
  .services-title, .hours-title {
    position: absolute;
    font-family: "Alegreya", serif;
    font-weight: 700;
    font-size: 25px;
    color: var(--heading-cyan);
  }
  .services-title { left: 41px; top: 178px; }
  .services-list {
    position: absolute;
    left: 41px;
    top: 254px;
    list-style: none;
    font-family: "Alegreya Sans", sans-serif;
    font-style: italic;
    font-weight: 300;
    font-size: 23px;
    line-height: 35px;
    color: var(--item-cyan);
  }
  .hours-title { left: 48px; top: 486px; }
  .hours {
    position: absolute;
    left: 48px;
    font-family: "Alegreya Sans", sans-serif;
    font-style: italic;
    font-weight: 300;
    font-size: 26px;
    line-height: 28px;
    color: var(--item-cyan);
  }
  .hours.weekdays { top: 537px; }
  .hours.sunday { top: 614px; }
  .contact {
    position: absolute;
    left: 10px;
    width: 464px;
    top: 940px;
    text-align: center;
    font-family: "Alegreya", serif;
    font-weight: 700;
    font-size: 25px;
    line-height: 32.5px;
    color: var(--navy);
  }
  .social {
    position: absolute;
    left: 36px;
    display: flex;
    align-items: center;
    gap: 10px;
    font-family: "Alegreya", serif;
    font-weight: 700;
    font-size: 26px;
    color: var(--navy);
  }
  .social.twitter { top: 1077px; }
  .social.facebook { top: 1120px; }
  .social-mark {
    width: 24px;
    height: 24px;
    border-radius: 4px;
    background: var(--navy);
  }
  .brand-mark {
    position: absolute;
    left: 577px;
    top: 846px;
    width: 160px;
    height: 160px;
    border-radius: 50%;
    background: var(--brand-dot);
  }
  .brand-name {
    position: absolute;
    left: 470px;
    width: 370px;
    top: 1020px;
    text-align: center;
    font-family: "Alegreya", serif;
    font-weight: 600;
    color: var(--brand);
    line-height: 1;
  }
  .brand-name .line-1 { display: block; font-size: 66px; }
  .brand-name .line-2 { display: block; font-size: 50px; margin-top: 4px; }
  .frame {
    position: absolute;
    inset: 0;
    border: 2px solid var(--frame);
    pointer-events: none;
  }
</style>
</head>
<body>
<main class="flyer">
  <svg class="waves" width="847" height="1200" viewBox="0 0 847 1200" aria-hidden="true">
    <path fill="var(--sky)" d="M0,0 L840,4 C760,140 690,330 640,520 C590,720 520,930 400,1060 C300,1160 160,1190 9,1194 L0,1200 Z"/>
    <path fill="var(--aqua)" d="M0,0 L840,4 C700,90 620,200 590,380 C560,560 560,700 480,860 C400,1020 220,1150 9,1194 L0,1200 Z"/>
    <path fill="var(--ocean)" d="M0,0 L840,4 C640,70 520,150 490,330 C465,480 475,600 420,740 C340,940 180,1090 9,1194 L0,1200 Z"/>
  </svg>

  <h2 class="services-title">Services We Offer:</h2>
  <ul class="services-list">
    <li>- Prescription Collection Service</li>
    <li>- Minor Ailments Scheme</li>
    <li>- Emergency Hormonal Contraception</li>
    <li>- Expert Health Advice</li>
    <li>- Medicines Disposal</li>
    <li>- Prescription Delivery Service</li>
  </ul>

  <h2 class="hours-title">TIMINGS:</h2>
  <p class="hours weekdays">MON - SAT<br>7:30 AM - 10:00 PM</p>
  <p class="hours sunday">SUNDAY<br>8:00 AM - 9 .00 PM</p>

  <address class="contact">
    Ashcombe Larkfield Centre,<br>
    Kestrel Row, Ashcombe, Nottingham,<br>
    NG4 2TW<br>
    0115 9630587
  </address>
  <p class="social twitter"><span class="social-mark"></span>ourthornfield</p>
  <p class="social facebook"><span class="social-mark"></span>ourthornfieldpharmacy</p>

  <div class="brand-mark"></div>
  <h1 class="brand-name"><span class="line-1">Thornfield</span><span class="line-2">Pharmacy</span></h1>

  <div class="frame"></div>
</main>
</body>
</html>
```